Sleek & Sexy MedSpa Direct Mailer Needed for High End Client

We need an eye catching and elegant direct mailer for our client Corva Lune Medical Spa. Please stay with black & white tones. They like Tessa Brimlow brand looks - sleek & sexy & high end.

Here is the template layout: https://quillvane.com/offering/coupon-mailer you can download a PDF or IDML on that page.

Website: https://corvalunemedicalspa.com/
Logo: https://files.dorvex.com/folders/7kqPz3Rt9Wm2Lx8Vb4Nc6Yh1Jd5Gs0FaE

Offers:
New Year/ New You! Make your beauty dreams a reality!
15% off laser hair removal packages
$50 off Velquin or Parelle
$75 off 1 Filler syringe
15% off KX products

Call today to learn more & make sure to mention MAIL OFFER!

```html
<!DOCTYPE html>
<html lang="en">
<head>
<meta charset="utf-8">
<title>Corva Lune Medical Spa – Mailer</title>
<link rel="stylesheet" href="https://fonts.googleapis.com/css2?family=Tinos:ital,wght@0,400;0,700;1,700&family=Courgette&display=swap">
<style>
:root{
  --stage:#a9a9a9;
  --ink:#0b0b0b;
  --paper-light:#f2f2f2;
  --paper-mid:#dcdcdc;
  --white:#ffffff;
  --peach-light:#fbe7d6;
  --peach:#e9b993;
  --skin:#c98e6d;
}
*{margin:0;padding:0;box-sizing:border-box}
html,body{width:921px;height:1200px;overflow:hidden;background:var(--stage)}
.mailer{
  position:absolute;left:30px;top:396px;width:860px;height:407px;
  background:linear-gradient(160deg,var(--paper-light) 0%,var(--paper-mid) 60%,var(--paper-light) 100%);
  overflow:hidden;font-family:"Tinos",serif;color:var(--ink);
  box-shadow:0 14px 28px rgba(0,0,0,.25);
}
.brand-tab{
  position:absolute;left:0;top:0;width:322px;height:78px;
  background:var(--ink);border-radius:0 39px 39px 0;
  display:flex;align-items:center;padding-left:38px;
}
.brand-name{color:var(--white);font-family:"Tinos",serif;font-weight:400;font-size:27px;letter-spacing:.5px}
.headline{
  position:absolute;left:47px;top:92px;font-family:"Courgette",cursive;
  font-size:21px;line-height:25px;color:var(--ink);
}
.headline .second{font-size:24px}
.offer{position:absolute;width:106px;height:106px}
.offer svg{position:absolute;inset:0}
.offer-text{
  position:absolute;inset:0;display:flex;flex-direction:column;align-items:center;justify-content:center;
  color:var(--white);text-align:center;padding-top:4px;
}
.offer-value{font-weight:700;font-size:32px;line-height:30px}
.offer-value.italic{font-style:italic}
.offer-off{font-family:"Courgette",cursive;font-size:11px;line-height:12px;margin-left:16px}
.offer-item{font-size:8px;line-height:9px}
.photo{
  position:absolute;left:401px;top:0;width:459px;height:313px;
  background:
    radial-gradient(ellipse 40% 45% at 55% 55%,var(--skin) 0%,rgba(201,142,109,.55) 45%,rgba(233,185,147,0) 75%),
    linear-gradient(90deg,rgba(242,242,242,1) 0%,rgba(251,231,214,.9) 30%,var(--peach-light) 70%,rgba(233,185,147,.7) 100%);
  -webkit-mask-image:linear-gradient(180deg,#000 75%,transparent 100%);
          mask-image:linear-gradient(180deg,#000 75%,transparent 100%);
}
.frame{position:absolute;left:388px;top:42px;width:323px;height:230px;border-left:4px solid var(--ink);border-top:4px solid var(--ink)}
.cta{position:absolute;left:395px;top:297px;font-weight:700;font-size:15.5px;letter-spacing:.2px}
.cta-strong{position:absolute;left:396px;top:317px;font-weight:700;font-style:italic;font-size:24px}
.contact-bar{
  position:absolute;left:388px;top:370px;width:472px;height:37px;background:var(--ink);
  border-radius:19px 0 0 19px;color:var(--white);display:flex;align-items:center;padding-left:12px;
}
.contact-bar svg{fill:var(--white);flex:none}
.phone{display:flex;align-items:center;gap:5px;font-size:14px;margin-right:16px}
.address{display:flex;align-items:center;gap:4px;font-size:7.5px;line-height:8.5px;margin-right:16px}
.web{display:flex;align-items:center;gap:4px;font-size:7.5px;margin-right:28px}
.socials{display:flex;gap:5px}
.socials span{width:7px;height:7px;border-radius:50%;background:var(--white)}
</style>
</head>
<body>
<main class="mailer">
  <div class="photo" role="img" aria-label="Photo of a relaxed spa client resting her head on a rolled towel in soft warm light"></div>
  <div class="frame"></div>

  <header class="brand-tab"><span class="brand-name">Corva Lune Medical Spa</span></header>

  <h1 class="headline">New Year/ New You! Make your<br><span class="second">beauty dreams a reality!</span></h1>

  <svg width="0" height="0" style="position:absolute">
    <defs>
      <g id="burst" fill="#0b0b0b">
        <rect x="15" y="15" width="76" height="76" transform="rotate(0 53 53)"/>
        <rect x="15" y="15" width="76" height="76" transform="rotate(15 53 53)"/>
        <rect x="15" y="15" width="76" height="76" transform="rotate(30 53 53)"/>
        <rect x="15" y="15" width="76" height="76" transform="rotate(45 53 53)"/>
        <rect x="15" y="15" width="76" height="76" transform="rotate(60 53 53)"/>
        <rect x="15" y="15" width="76" height="76" transform="rotate(75 53 53)"/>
      </g>
    </defs>
  </svg>

  <div class="offer" style="left:34px;top:161px">
    <svg viewBox="0 0 106 106"><use href="#burst"/></svg>
    <div class="offer-text"><span class="offer-value italic">15%</span><span class="offer-off">OFF</span><span class="offer-item">laser hair<br>removal packages</span></div>
  </div>
  <div class="offer" style="left:177px;top:161px">
    <svg viewBox="0 0 106 106"><use href="#burst"/></svg>
    <div class="offer-text"><span class="offer-value">$50</span><span class="offer-off">OFF</span><span class="offer-item">Velquin or Parelle</span></div>
  </div>
  <div class="offer" style="left:34px;top:279px">
    <svg viewBox="0 0 106 106"><use href="#burst"/></svg>
    <div class="offer-text"><span class="offer-value">$75</span><span class="offer-off">OFF</span><span class="offer-item">1 Filler syringe</span></div>
  </div>
  <div class="offer" style="left:177px;top:279px">
    <svg viewBox="0 0 106 106"><use href="#burst"/></svg>
    <div class="offer-text"><span class="offer-value italic">15%</span><span class="offer-off">OFF</span><span class="offer-item">KX products</span></div>
  </div>

  <p class="cta">Call today to learn more &amp; &nbsp;make sure to mention</p>
  <p class="cta-strong">MAIL OFFER!</p>

  <footer class="contact-bar">
    <div class="phone">
      <svg width="9" height="9" viewBox="0 0 24 24"><path d="M6.6 10.8a15.1 15.1 0 0 0 6.6 6.6l2.2-2.2c.3-.3.7-.4 1-.2 1.1.4 2.3.6 3.6.6.6 0 1 .4 1 1V20c0 .6-.4 1-1 1A17 17 0 0 1 3 4c0-.6.4-1 1-1h3.5c.6 0 1 .4 1 1 0 1.3.2 2.5.6 3.6.1.3 0 .7-.2 1z"/></svg>
      401-555-0172
    </div>
    <div class="address">
      <svg width="7" height="9" viewBox="0 0 24 32"><path d="M12 0C5.4 0 0 5.4 0 12c0 9 12 20 12 20s12-11 12-20C24 5.4 18.6 0 12 0zm0 17a5 5 0 1 1 0-10 5 5 0 0 1 0 10z"/></svg>
      <span>1480 Harbor Lane<br>Eastmoor, RI 02890</span>
    </div>
    <div class="web">
      <svg width="8" height="8" viewBox="0 0 24 24"><circle cx="12" cy="12" r="10" fill="none" stroke="#fff" stroke-width="2"/><path d="M2 12h20M12 2c3 3 3 17 0 20M12 2c-3 3-3 17 0 20" fill="none" stroke="#fff" stroke-width="2"/></svg>
      corvalunemedicalspa.com
    </div>
    <div class="socials" aria-label="Social media"><span></span><span></span><span></span></div>
  </footer>
</main>
</body>
</html>
```